Torven Medical needs bold attention catching website for healthcare professionals(target)

I need a hero page as well as a products and about page for a website of mine. I specialize in orthopedic instruments . Specifically bone drills and saws. This whole company was founded to bring superb quality highly discounted medical instruments. Specifically bone drills, bone saws, k-wires and pins. Two main points should be cost savings and superior quality.

Target Market(s)

healthcare professionals Surgeons and hospital material managers

Number of Pages Required

3 page

Font styles to use
Serif

Colors

Designer to choose colors to be used in the design.

Requirements
Must have
• colors should match logo design

```html
<!DOCTYPE html>
<html lang="en">
<head>
<meta charset="utf-8">
<title>Torven Medical</title>
<link href="https://fonts.googleapis.com/css2?family=Mulish:wght@300;400;600;700;800&family=Work+Sans:wght@700;800&display=swap" rel="stylesheet">
<style>
:root{
  --orange:#E8994B;
  --orange-strong:#F18A24;
  --ink:#1B1B1B;
  --white:#FFFFFF;
  --sand:#F2EFEC;
  --stone:#E9E7E5;
  --footer:#1D1D1D;
  --footer-text:#9A9A9A;
}
*{margin:0;padding:0;box-sizing:border-box}
html,body{width:1200px;height:2294px;overflow:hidden;background:var(--white)}
body{font-family:"Mulish",sans-serif;color:var(--ink)}
.page{position:relative;width:1200px;height:2294px;overflow:hidden}
.abs{position:absolute}

/* hero */
.hero{left:0;top:0;width:1200px;height:550px;
  background:linear-gradient(100deg,#F7F8FA 0%,#F4F5F7 45%,#E6EAEE 62%,#F3B57A 74%,#DCE2E8 84%,#F0923A 94%,#F6F7F9 100%)}
.brand{left:118px;top:38px;display:flex;align-items:center;gap:8px;font-size:22px;font-weight:600;color:var(--ink);letter-spacing:.5px}
.brand-dot{width:12px;height:12px;border-radius:50%;background:var(--orange-strong)}
.nav{top:48px;left:371px;display:flex;gap:30px;font-size:12.5px;letter-spacing:.4px}
.nav a{color:var(--ink);text-decoration:none;padding-bottom:4px}
.nav a.active{border-bottom:1.5px solid var(--ink)}
.call{left:819px;top:37px;width:287px;height:35px;background:var(--orange-strong);color:var(--white);font-size:11px;font-weight:700;letter-spacing:.4px;display:flex;align-items:center;justify-content:center}
.hero-title{left:143px;top:245px;font-family:"Work Sans",sans-serif;font-weight:800;font-size:26.5px;line-height:35px;letter-spacing:.6px;color:var(--ink)}
.btn-outline{border:2px solid var(--ink);display:flex;align-items:center;justify-content:center;font-size:11px;font-weight:800;letter-spacing:1.2px;color:var(--ink)}
.hero-btn{left:145px;top:372px;width:196px;height:36px}

/* welcome */
.welcome{left:0;top:550px;width:1200px;height:334px;background:var(--orange);color:var(--white);text-align:center}
.welcome h2{position:absolute;top:50px;width:100%;font-weight:300;font-size:27px}
.welcome p{position:absolute;left:293px;top:93px;width:614px;font-size:14.5px;line-height:20.3px;font-weight:400}
.read-more{left:507px;top:241px;width:175px;height:36px;border:2px solid var(--ink);background:#F1F3F6;display:flex;align-items:center;justify-content:center;gap:12px;font-size:11.5px;font-weight:700;letter-spacing:1px;color:var(--ink)}

/* why */
.why-bg-left{left:0;top:884px;width:760px;height:478px;background:var(--sand)}
.why-bg-right{left:760px;top:884px;width:440px;height:478px;background:var(--stone)}
.why-photo{left:417px;top:1006px;width:602px;height:401px;background:linear-gradient(180deg,#F6EFD9 0%,#E9D6B4 40%,#C9A57B 70%,#8D7560 100%)}
.photo-brand{left:570px;top:1134px;font-size:21px;font-weight:600;color:var(--ink);display:flex;align-items:center;gap:8px}
.tag{background:#111;color:var(--white);font-size:16px;padding:3px 8px;height:26px;white-space:nowrap}
.why-card{left:154px;top:945px;width:344px;height:339px;background:var(--white);border:1px solid #ECECEC}
.why-card h3{position:absolute;left:47px;top:48px;font-size:19px;font-weight:600}
.why-list{position:absolute;left:43px;top:93px;list-style:none}
.why-list li{display:flex;align-items:center;gap:12px;height:41.3px;font-size:15px}

/* products */
.est-title{left:95px;top:1508px;font-size:20px;font-weight:700;letter-spacing:.3px}
.est-sub{left:95px;top:1542px;font-size:16px}
.est-sub span{color:var(--orange-strong)}
.btn-line{left:874px;top:1530px;width:233px;height:38px;border:2px solid var(--orange-strong);color:var(--orange-strong);font-size:11.5px;font-weight:600;letter-spacing:1.3px;display:flex;align-items:center;justify-content:center}
.card{top:1598px;width:233px;height:194px;border:2px solid var(--ink);background:var(--white)}
.card-img{position:absolute;left:14px;top:12px;width:200px;height:150px;background:linear-gradient(135deg,#FFFFFF 0%,#E3E6E9 50%,#FFFFFF 100%)}
.enquiry{position:absolute;right:20px;bottom:34px;font-size:10px;font-weight:700;display:flex;align-items:center;gap:4px}
.details{position:absolute;right:-1px;bottom:-1px;width:95px;height:26px;background:var(--ink);color:var(--white);font-size:9px;font-weight:700;letter-spacing:1.2px;display:flex;align-items:center;justify-content:center}

/* contact */
.rule{left:92px;top:1918px;width:1015px;height:2px;background:var(--ink)}
.info{left:95px;top:1940px;font-size:20.5px;line-height:29.5px;letter-spacing:.2px}
.btn-fill{left:883px;top:1965px;width:224px;height:38px;background:var(--orange-strong);color:var(--white);font-size:11.5px;font-weight:600;letter-spacing:1.3px;display:flex;align-items:center;justify-content:center}

/* footer */
.footer{left:0;top:2124px;width:1200px;height:170px;background:var(--footer);text-align:center}
.footer-nav{position:absolute;top:34px;width:100%;display:flex;justify-content:center;gap:21px;font-size:12.5px;letter-spacing:.8px;color:var(--footer-text)}
.copyright{position:absolute;top:65px;width:100%;color:#D8D8D8;font-size:14.5px;letter-spacing:.4px}
.social{position:absolute;top:114px;left:519px;display:flex;gap:5px}
.social span{width:33px;height:33px;border-radius:50%;background:#3A3A3A}
</style>
</head>
<body>
<div class="page">

  <section class="abs hero" role="img" aria-label="Photograph of a gold bone drill and a steel k-wire standing against folded orange and white paper shapes"></section>
  <div class="abs brand"><span class="brand-dot"></span>Torven Medical</div>
  <nav class="abs nav">
    <a class="active">Home</a><a>About Us</a><a>Our Product Catalog</a><a>Contact us</a>
  </nav>
  <div class="abs call">FOR ANY QUERY CALL US AT : +01 5550142387</div>
  <h1 class="abs hero-title">We provide<br>Cost Savings &amp; Superior<br>Quality Orthopedic Instruments</h1>
  <div class="abs btn-outline hero-btn">VIEW PRODUCT CATALOG</div>

  <section class="abs welcome">
    <h2>Welcome to Torven Medical website</h2>
    <p>Hospitals are increasingly seeking ways to cut cost while continuing to deliver high quality medical care.&nbsp; Torven Medical was created to offer hospitals and physicians high-quality products at a significantly lower cost. Torven Medical focus is on the orthopedic disposable market by providing quality generic products that are utilized to replace many legacy products that have low physician preference and are subject to 5%-10% annual unsustainable price increases.</p>
    <div class="abs read-more">READ MORE
      <svg width="40" height="12" viewBox="0 0 40 12"><path d="M0 6H38M32 1l6 5-6 5" fill="none" stroke="#1B1B1B" stroke-width="1.4"/></svg>
    </div>
  </section>

  <div class="abs why-bg-left"></div>
  <div class="abs why-bg-right"></div>
  <div class="abs why-photo" role="img" aria-label="Photograph of a runner in a teal jacket on an open road at sunset"></div>
  <div class="abs photo-brand"><span class="brand-dot"></span>Torven Medical</div>
  <div class="abs tag" style="left:559px;top:1214px">Orthopedic Implant</div>
  <div class="abs tag" style="left:559px;top:1244px">Manufacturers, Suppliers &amp; Exporter</div>
  <div class="abs why-card">
    <h3>Why choose us?</h3>
    <ul class="why-list">
      <li><svg width="30" height="30" viewBox="0 0 30 30"><circle cx="15" cy="15" r="14" fill="none" stroke="#1B1B1B" stroke-width="1.3"/><path d="M10 15.5l3.5 3.5 7-8" fill="none" stroke="#1B1B1B" stroke-width="1.3"/></svg>Lowest Price Guarantee</li>
      <li><svg width="30" height="30" viewBox="0 0 30 30"><circle cx="15" cy="15" r="14" fill="none" stroke="#1B1B1B" stroke-width="1.3"/><path d="M10 15.5l3.5 3.5 7-8" fill="none" stroke="#1B1B1B" stroke-width="1.3"/></svg>100% Satisfaction Guarantee</li>
      <li><svg width="30" height="30" viewBox="0 0 30 30"><circle cx="15" cy="15" r="14" fill="none" stroke="#1B1B1B" stroke-width="1.3"/><path d="M10 15.5l3.5 3.5 7-8" fill="none" stroke="#1B1B1B" stroke-width="1.3"/></svg>Highest Quality Products</li>
      <li><svg width="30" height="30" viewBox="0 0 30 30"><circle cx="15" cy="15" r="14" fill="none" stroke="#1B1B1B" stroke-width="1.3"/><path d="M10 15.5l3.5 3.5 7-8" fill="none" stroke="#1B1B1B" stroke-width="1.3"/></svg>Our in-house production unit</li>
      <li><svg width="30" height="30" viewBox="0 0 30 30"><circle cx="15" cy="15" r="14" fill="none" stroke="#1B1B1B" stroke-width="1.3"/><path d="M10 15.5l3.5 3.5 7-8" fill="none" stroke="#1B1B1B" stroke-width="1.3"/></svg>Excellent Service</li>
    </ul>
  </div>

  <h2 class="abs est-title">Established Supplier with Over 15+ years Experience.</h2>
  <p class="abs est-sub">We at <span>TORVEN MEDICAL</span> offer quality Orthopaedic Trauma Implants in a wide range.</p>
  <div class="abs btn-line">VIEW ALL OUR PRODUCTS</div>

  <div class="abs card" style="left:92px">
    <div class="card-img" role="img" aria-label="Product photo of bone cutting forceps"></div>
    <div class="enquiry">Send Enquiry <svg width="6" height="9" viewBox="0 0 6 9"><path d="M1 1l3.5 3.5L1 8" fill="none" stroke="#1B1B1B" stroke-width="1.5"/></svg></div>
    <div class="details">VIEW DETAILS</div>
  </div>
  <div class="abs card" style="left:353px">
    <div class="card-img" role="img" aria-label="Product photo of bone rongeur"></div>
    <div class="enquiry">Send Enquiry <svg width="6" height="9" viewBox="0 0 6 9"><path d="M1 1l3.5 3.5L1 8" fill="none" stroke="#1B1B1B" stroke-width="1.5"/></svg></div>
    <div class="details">VIEW DETAILS</div>
  </div>
  <div class="abs card" style="left:613px">
    <div class="card-img" role="img" aria-label="Product photo of a wire tensioner instrument"></div>
    <div class="enquiry">Send Enquiry <svg width="6" height="9" viewBox="0 0 6 9"><path d="M1 1l3.5 3.5L1 8" fill="none" stroke="#1B1B1B" stroke-width="1.5"/></svg></div>
    <div class="details">VIEW DETAILS</div>
  </div>
  <div class="abs card" style="left:873px">
    <div class="card-img" role="img" aria-label="Product photo of a bone drill bit"></div>
    <div class="enquiry">Send Enquiry <svg width="6" height="9" viewBox="0 0 6 9"><path d="M1 1l3.5 3.5L1 8" fill="none" stroke="#1B1B1B" stroke-width="1.5"/></svg></div>
    <div class="details">VIEW DETAILS</div>
  </div>

  <div class="abs rule"></div>
  <p class="abs info">For more information about our surgical instrument<br>refurbishment programme please email hello@torvenmail.example<br>or call us on + (0) 155 5014238.</p>
  <div class="abs btn-fill">GET IN TOUCH WITH US</div>

  <footer class="abs footer">
    <div class="footer-nav"><span>Home</span><span>About Us</span><span>Our Product Catalog</span><span>Contact us</span></div>
    <div class="copyright">© Torven Medical 2019. All Rights Reserved</div>
    <div class="social" aria-label="Social links">
      <span></span><span></span><span></span><span></span>
    </div>
  </footer>

</div>
</body>
</html>
```